Create Oceanfront SEO Website – Marlow Haven

I am web developer to build a high-quality, SEO-optimized website. The site is fully structured with content, layout, and purpose clearly defined, and comes with keyword-rich SEO guidance to maximize search engine visibility. Domain names and page content are provided.

Developer Role:
Build a responsive, fast-loading website in WordPress, allowing us to edit and update content in the future.
Implement SEO best practices, including meta tags, structured data, and optimized content.
Ensure smooth navigation, intuitive UX, and visually appealing design.
Establish the website to a fully functional state, after which we will handle ongoing updates and changes.
Domain and website will be hosted by hostwren under my profile.
Key Highlights:
Structured website with ready-to-use content.
SEO-focused pages for maximum visibility.
Domains and site structure already defined.
Creative freedom in design within the provided framework.

Target Market(s)

vacationers

Industry/Entity Type

vacation and travel

Coding

Coded - Design and coding required

Colors
0054AA
0677BA
7BADD7
CADEEF
E8F1F8
0094D4
00A9DD
6FCCEA
C7EBF8
E9F6FB
00AB8E
00BBA5
67D7C9
C6EFE9
E9F9F6
FFF300
FFF600
FEFA6F
FFFEC7
FFFEE8

Requirements
Must have
• see brief

```html
<!DOCTYPE html>
<html lang="en">
<head>
<meta charset="utf-8">
<title>Marlow Haven – Oceanfront Condo</title>
<link href="https://fonts.googleapis.com/css2?family=Arimo:wght@400;700&display=swap" rel="stylesheet">
<style>
:root{
  --blue:#1b6fb7;
  --blue-deep:#0054aa;
  --navy:#1b3f8f;
  --teal:#3cc3b2;
  --ice:#e8f1f8;
  --ice-2:#eef3f9;
  --icon-bg:#dfe8f3;
  --ink:#1c1c1c;
  --text:#333;
  --white:#fff;
  --black:#000;
}
*{box-sizing:border-box;margin:0;padding:0}
html,body{width:1200px;height:4950px;overflow:hidden}
body{font-family:"Arimo",Arial,sans-serif;color:var(--text);background:var(--white);position:relative}
.abs{position:absolute}
a{color:inherit;text-decoration:none}

/* top bar */
.topbar{position:absolute;left:0;top:0;width:1200px;height:42px;background:var(--blue);color:var(--white);font-size:14px;font-weight:700}
.topbar .item{position:absolute;top:13px;display:flex;align-items:center;gap:10px}
.topbar .social{position:absolute;right:132px;top:13px;display:flex;gap:10px}
.topbar .social span{width:16px;height:16px;border-radius:50%;background:var(--white)}

/* header */
.header{position:absolute;left:0;top:42px;width:1200px;height:85px;background:var(--white)}
.logo{position:absolute;left:110px;top:25px;font-size:29px;font-weight:700;color:var(--blue)}
.nav{position:absolute;left:479px;top:32px;display:flex;gap:23px;font-size:15px;color:var(--ink)}
.nav .active{color:var(--blue);font-weight:700}
.btn-contact{position:absolute;left:954px;top:21px;width:134px;height:45px;border-radius:23px;background:var(--blue);color:var(--white);font-weight:700;font-size:15px;display:flex;align-items:center;justify-content:center}

/* hero */
.hero{position:absolute;left:0;top:127px;width:1200px;height:594px;overflow:hidden}
.hero-photo{position:absolute;inset:0;background:linear-gradient(100deg,#4a3a32 0%,#7a6250 30%,#c79a6d 52%,#8d7462 70%,#3d2c24 100%)}
.hero-shape{position:absolute;left:0;top:0}
.hero h1{position:absolute;left:110px;top:120px;width:600px;font-size:42px;line-height:51px;color:var(--white);font-weight:700}
.hero p{position:absolute;left:110px;top:232px;width:520px;font-size:15px;line-height:27px;color:var(--white)}
.hero .btns{position:absolute;left:110px;top:307px;display:flex;gap:10px}
.pill{height:39px;border-radius:20px;color:var(--white);font-weight:700;font-size:14px;display:flex;align-items:center;justify-content:center;padding:0 16px;white-space:nowrap}
.pill.blue{background:var(--blue)}
.pill.teal{background:var(--teal)}
.pill.navy{background:var(--navy)}
.pill.outline{border:2px solid rgba(255,255,255,.6)}

/* headings */
.sec-title{position:absolute;left:0;width:1200px;text-align:center;font-size:34px;color:var(--ink);font-weight:400}
.sec-title b{color:var(--blue);font-weight:700}
.rule{position:absolute;left:558px;width:84px;height:3px;background:var(--blue)}

/* welcome */
.welcome-copy{position:absolute;left:165px;top:886px;width:870px;text-align:center;font-size:15px;line-height:28.5px;color:var(--ink)}
.circle{position:absolute;top:1046px;width:292px;height:292px;border-radius:50%;overflow:hidden}
.circle .label{position:absolute;left:0;width:100%;top:226px;text-align:center;color:var(--white);font-size:20px;display:flex;justify-content:center;align-items:center;gap:8px}
.circle .label.dark{color:var(--ink)}
.circle svg.icon{position:absolute;left:116px;top:100px}

/* explore */
.explore{position:absolute;left:0;top:1454px;width:1200px;height:521px;background:var(--navy)}
.explore h2{position:absolute;left:0;top:88px;width:1200px;text-align:center;color:var(--white);font-size:31px;font-weight:400}
.explore .rule-w{position:absolute;left:570px;top:143px;width:60px;height:3px;background:var(--white)}
.explore p{position:absolute;left:165px;top:170px;width:870px;text-align:center;color:var(--white);font-size:13.5px;line-height:25.5px}
.explore .btns{position:absolute;left:342px;top:275px;display:flex;gap:10px}
.explore .pill{height:40px;font-size:14px}
.frame{position:absolute;left:163px;top:1812px;width:875px;height:392px;border:4px solid var(--white);background:linear-gradient(180deg,#2f6f8a 0%,#4f93a8 35%,#d7e4e6 60%,#6fa0b0 100%)}

/* why */
.card{position:absolute;width:298px;height:224px;background:var(--white);border:1px solid #e2e2e2;box-shadow:0 2px 8px rgba(0,0,0,.12);text-align:center}
.card .ico{position:absolute;left:111px;top:33px;width:76px;height:76px;border-radius:50%;background:var(--icon-bg);display:flex;align-items:center;justify-content:center}
.card p{position:absolute;left:20px;top:135px;width:256px;font-size:17px;line-height:31px;color:var(--ink)}
.card.featured{background:#1f5ea8;border-color:#1f5ea8}
.card.featured .ico{background:var(--white)}
.card.featured p{color:var(--white)}
.repeat{position:absolute;left:344px;top:2898px;width:510px;height:48px;border-radius:24px;background:var(--navy);color:var(--white);font-weight:700;font-size:15px;display:flex;align-items:center;justify-content:center}

/* testimonials */
.testi{position:absolute;left:0;top:3029px;width:1200px;height:594px;background:var(--ice-2)}
.t-card{position:absolute;top:3240px;width:304px;height:279px;background:var(--white);box-shadow:0 2px 8px rgba(0,0,0,.12);text-align:center}
.avatar{position:absolute;top:3196px;width:123px;height:123px;border-radius:50%;border:5px solid var(--white);box-shadow:0 2px 6px rgba(0,0,0,.15)}
.t-card .stars{position:absolute;left:0;width:100%;top:103px;color:#f2b300;font-size:16px;letter-spacing:1px}
.t-card h4{position:absolute;left:0;width:100%;top:130px;font-size:17px;color:var(--ink)}
.t-card p{position:absolute;left:18px;width:268px;top:160px;font-size:14px;line-height:24px;color:var(--ink)}
.arrow{position:absolute;top:3378px;width:25px;height:25px;border:1.5px solid #666;border-radius:50%;display:flex;align-items:center;justify-content:center}

/* gallery */
.g{position:absolute;border-radius:10px}
.read-more{position:absolute;left:521px;top:4279px;width:156px;height:42px;border-radius:21px;background:var(--navy);color:var(--white);font-size:14px;font-weight:700;display:flex;align-items:center;justify-content:center;gap:8px;letter-spacing:.5px}

/* footer */
.footer-shape{position:absolute;left:0;top:4300px}
.f-head{position:absolute;top:4574px;color:var(--white);font-size:22px;font-weight:700}
.f-list{position:absolute;top:4612px;list-style:none;color:var(--white);font-size:14px}
.f-list li{height:31px;display:flex;align-items:center;gap:10px}
.f-contact{position:absolute;left:490px;color:var(--white);font-size:14px;display:flex;align-items:center;gap:14px}
.f-contact .dot{width:34px;height:34px;border-radius:50%;background:var(--white);display:flex;align-items:center;justify-content:center}
.news-copy{position:absolute;left:810px;top:4622px;width:290px;color:var(--white);font-size:14px;line-height:29px}
.news-label{position:absolute;left:814px;top:4694px;color:var(--white);font-size:14px}
.news-line{position:absolute;left:810px;top:4722px;width:273px;height:1px;background:#aaa}
.subscribe{position:absolute;left:819px;top:4755px;width:144px;height:48px;border-radius:24px;background:var(--white);color:var(--black);font-weight:700;font-size:16px;display:flex;align-items:center;justify-content:center}
.f-rule{position:absolute;left:98px;top:4879px;width:1002px;height:1px;background:#777}
.copyright{position:absolute;left:0;top:4906px;width:1200px;text-align:center;color:var(--white);font-size:14px}
</style>
</head>
<body>

<div class="topbar">
  <div class="item" style="left:115px">
    <svg width="16" height="16" viewBox="0 0 24 24"><path fill="#fff" d="M6.6 10.8a15 15 0 0 0 6.6 6.6l2.2-2.2a1 1 0 0 1 1-.25 11.4 11.4 0 0 0 3.6.57 1 1 0 0 1 1 1V20a1 1 0 0 1-1 1A17 17 0 0 1 3 4a1 1 0 0 1 1-1h3.5a1 1 0 0 1 1 1c0 1.25.2 2.45.57 3.57a1 1 0 0 1-.25 1z"/></svg>
    PHONE: +1888 8888 8888
  </div>
  <div class="item" style="left:375px">
    <svg width="18" height="14" viewBox="0 0 24 18"><rect x="0" y="0" width="24" height="18" rx="2" fill="#fff"/><path d="M1 2l11 8 11-8" stroke="#1b6fb7" stroke-width="2" fill="none"/></svg>
    EMAIL: info@companyname.com
  </div>
  <div class="social" aria-label="Social links"><span></span><span></span><span></span><span></span></div>
</div>

<header class="header">
  <div class="logo">Marlow Haven</div>
  <nav class="nav">
    <a class="active">Home</a><a>About</a><a>Things to Do</a><a>Attractions</a><a>Events</a><a>Blog</a>
  </nav>
  <a class="btn-contact">Contact Us</a>
</header>

<section class="hero">
  <div class="hero-photo" role="img" aria-label="Oceanfront condo balcony with a lounge chair overlooking the beach at sunset"></div>
  <svg class="hero-shape" width="1200" height="594" viewBox="0 0 1200 594">
    <path d="M0,440 Q600,672 1200,440 L1200,594 L0,594 Z" fill="#fff"/>
    <path d="M173,517 Q600,671 1030,517 Q600,633 173,517 Z" fill="#1b6fb7"/>
  </svg>
  <h1>Stay in Our Marlow Beach Oceanfront Condo</h1>
  <p>Your perfect Marlow Beach getaway — ocean views, modern amenities, and steps from the sand.</p>
  <div class="btns">
    <a class="pill blue outline" style="width:138px">Book on StayNest</a>
    <a class="pill teal outline" style="width:134px">Book on HomeHop</a>
    <a class="pill navy outline" style="width:217px">Book on Lodge Locator</a>
  </div>
</section>

<section class="welcome">
  <h2 class="sec-title" style="top:811px">Welcome to Your <b>Marlow Beach Vacation Home</b></h2>
  <div class="rule" style="top:864px"></div>
  <p class="welcome-copy">Welcome to your coastal retreat, perfectly situated just steps from the beach. This pet-friendly property offers stunning ocean views and the convenience of a short walk to the shoreline, making it ideal for both relaxation and adventure. Whether you're unwinding on the balcony or strolling with your pup along the sand, this getaway blends comfort with an unbeatable location.</p>

  <div class="circle" style="left:160px;background:linear-gradient(180deg,#3d9f92 0%,#5fb7a4 55%,#8cc9b0 100%)" role="img" aria-label="Beach pier at sunrise">
    <svg class="icon" width="60" height="50" viewBox="0 0 60 50" fill="none" stroke="#fff" stroke-width="2"><path d="M8 22a22 14 0 0 1 44 0z"/><path d="M30 8v36M14 44h32M4 48h52"/><circle cx="52" cy="6" r="3"/></svg>
    <div class="label">Beach <svg width="18" height="18" viewBox="0 0 20 20"><circle cx="10" cy="10" r="9" fill="#fff"/><path d="M6 10h7M10 6l4 4-4 4" stroke="#3d9f92" stroke-width="2" fill="none"/></svg></div>
  </div>
  <div class="circle" style="left:435px;background:radial-gradient(circle at 50% 45%,#f4ef5e 0%,#e7e138 70%,#dcd52e 100%)" role="img" aria-label="Bright local restaurant interior">
    <svg class="icon" width="62" height="56" viewBox="0 0 62 56" fill="none" stroke="#222" stroke-width="2"><path d="M6 18h50l-4-12H10z"/><path d="M8 18v34h46V18M16 30h10v22M34 30h12v10H34z"/><path d="M20 6v-4M42 6v-4"/></svg>
    <div class="label dark">Local Restaurants <svg width="18" height="18" viewBox="0 0 20 20"><circle cx="10" cy="10" r="9" fill="#222"/><path d="M6 10h7M10 6l4 4-4 4" stroke="#e7e138" stroke-width="2" fill="none"/></svg></div>
  </div>
  <div class="circle" style="left:719px;background:linear-gradient(160deg,#4a65a0 0%,#2d4f8a 45%,#5a7ea0 70%,#2b4a82 100%)" role="img" aria-label="Aerial view of the coastline and town">
    <svg class="icon" width="50" height="60" viewBox="0 0 50 60" fill="none" stroke="#fff" stroke-width="2"><rect x="14" y="4" width="22" height="52"/><path d="M14 16h22M14 28h22M14 40h22M25 4v52M6 56h38"/></svg>
    <div class="label">Attractions <svg width="18" height="18" viewBox="0 0 20 20"><circle cx="10" cy="10" r="9" fill="#fff"/><path d="M6 10h7M10 6l4 4-4 4" stroke="#2d4f8a" stroke-width="2" fill="none"/></svg></div>
  </div>
</section>

<section class="explore">
  <h2>Explore Marlow <b>Beach, Florida</b></h2>
  <div class="rule-w"></div>
  <p>Marlow Beach is a charming seaside town on Florida's Atlantic coast. Known for its historic fishing pier, scenic A1A highway, family-friendly beaches, and local eateries, it's a peaceful alternative to crowded tourist destinations. Visitors love strolling the pier, enjoying fresh seafood, and exploring nearby parks and nature trails.</p>
  <div class="btns">
    <a class="pill blue outline" style="width:139px">Book on StayNest</a>
    <a class="pill teal outline" style="width:135px">Book on HomeHop</a>
    <a class="pill blue outline" style="width:221px">Book on Lodge Locator</a>
  </div>
</section>
<div class="frame" role="img" aria-label="Two girls riding bodyboards through breaking ocean waves"></div>

<section class="why">
  <h2 class="sec-title" style="top:2282px">Why Our Condo Is <b>Perfect for Your Stay</b></h2>
  <div class="rule" style="top:2332px;left:570px;width:60px"></div>

  <div class="card" style="left:117px;top:2365px">
    <div class="ico"><svg width="36" height="36" viewBox="0 0 36 36" fill="none" stroke="#1b6fb7" stroke-width="2"><rect x="6" y="6" width="24" height="26"/><path d="M6 12h24M12 12v20M18 12v20M24 12v20M3 32h30"/></svg></div>
    <p>Oceanfront balcony with panoramic Atlantic views</p>
  </div>
  <div class="card featured" style="left:448px;top:2365px">
    <div class="ico"><svg width="36" height="36" viewBox="0 0 36 36" fill="none" stroke="#1b6fb7" stroke-width="2"><path d="M6 30h24M10 30V16l8-8 8 8v14"/><circle cx="18" cy="20" r="4"/></svg></div>
    <p>Pet-friendly accommodations for dogs</p>
  </div>
  <div class="card" style="left:781px;top:2365px">
    <div class="ico"><svg width="36" height="36" viewBox="0 0 36 36" fill="none" stroke="#1b6fb7" stroke-width="2"><path d="M8 16a10 7 0 0 1 20 0z"/><path d="M18 9v22M4 31h28"/><circle cx="28" cy="6" r="2.5"/></svg></div>
    <p>Steps from Marlow Beach shoreline</p>
  </div>
  <div class="card" style="left:117px;top:2623px">
    <div class="ico"><svg width="36" height="36" viewBox="0 0 36 36" fill="none" stroke="#1b6fb7" stroke-width="2"><rect x="6" y="6" width="24" height="26"/><path d="M6 12h24M12 12v20M18 12v20M24 12v20M3 32h30"/></svg></div>
    <p>Fully furnished kitchen and modern appliances</p>
  </div>
  <div class="card" style="left:448px;top:2623px">
    <div class="ico"><svg width="36" height="36" viewBox="0 0 36 36" fill="none" stroke="#1b6fb7" stroke-width="2"><path d="M4 18h28v4a8 8 0 0 1-8 8H12a8 8 0 0 1-8-8z"/><path d="M26 18V6h4M10 30l-2 4M26 30l2 4"/></svg></div>
    <p>Spacious living area, bedrooms, and bathrooms</p>
  </div>
  <div class="card" style="left:781px;top:2623px">
    <div class="ico"><svg width="36" height="36" viewBox="0 0 36 36" fill="none" stroke="#1b6fb7" stroke-width="2"><path d="M8 16a10 7 0 0 1 20 0z"/><path d="M18 9v22M4 31h28"/><circle cx="28" cy="6" r="2.5"/></svg></div>
    <p>Free parking and easy access to local shops and restaurants</p>
  </div>
  <a class="repeat">Repeat booking buttons here: StayNest | HomeHop | Lodge Locator</a>
</section>

<section class="testi"></section>
<h2 class="sec-title" style="top:3092px">Client <b>Testimonials</b></h2>
<div class="rule" style="top:3145px;left:564px;width:72px"></div>
<div class="arrow" style="left:44px"><svg width="10" height="10" viewBox="0 0 10 10"><path d="M7 1L3 5l4 4" stroke="#666" stroke-width="1.5" fill="none"/></svg></div>
<div class="arrow" style="left:1131px"><svg width="10" height="10" viewBox="0 0 10 10"><path d="M3 1l4 4-4 4" stroke="#666" stroke-width="1.5" fill="none"/></svg></div>

<div class="t-card" style="left:112px"><div class="stars">★★★★★</div><h4>John Smith</h4><p>Lorem ipsum dolor sit amet, consectetur adipiscing elit, sed do eiusmod tempor incididunt ut labore et dolore magna aliqua.</p></div>
<div class="t-card" style="left:448px"><div class="stars">★★★★★</div><h4>John Smith</h4><p>Lorem ipsum dolor sit amet, consectetur adipiscing elit, sed do eiusmod tempor incididunt ut labore et dolore magna aliqua.</p></div>
<div class="t-card" style="left:785px"><div class="stars">★★★★★</div><h4>John Smith</h4><p>Lorem ipsum dolor sit amet, consectetur adipiscing elit, sed do eiusmod tempor incididunt ut labore et dolore magna aliqua.</p></div>
<div class="avatar" style="left:202px;background:linear-gradient(180deg,#d9d4cf 0%,#b0744a 60%,#8a4a2a 100%)" role="img" aria-label="Guest portrait"></div>
<div class="avatar" style="left:538px;background:linear-gradient(180deg,#cfd6dc 0%,#8e9aa3 60%,#3d5566 100%)" role="img" aria-label="Guest portrait"></div>
<div class="avatar" style="left:875px;background:linear-gradient(180deg,#4fb3e8 0%,#3a9ad4 55%,#e3a23a 100%)" role="img" aria-label="Guest portrait"></div>

<section class="gallery">
  <h2 class="sec-title" style="top:3697px">Our <b>Gallery</b></h2>
  <div class="g" style="left:112px;top:3777px;width:298px;height:227px;background:linear-gradient(180deg,#6b8fb0 0%,#3e5a3a 40%,#1f8fd0 75%,#3aa9e0 100%)" role="img" aria-label="Palm-lined resort swimming pool"></div>
  <div class="g" style="left:421px;top:3777px;width:419px;height:227px;background:linear-gradient(180deg,#2c6a8a 0%,#8fa9b4 25%,#a6a49a 55%,#7a7f76 100%)" role="img" aria-label="Aerial view of the beachfront neighborhood"></div>
  <div class="g" style="left:852px;top:3777px;width:236px;height:227px;background:linear-gradient(180deg,#3a2a26 0%,#b5552a 45%,#e58b3a 60%,#5a2f1e 100%)" role="img" aria-label="Sunset over the ocean and pier"></div>
  <div class="g" style="left:112px;top:4019px;width:298px;height:225px;background:linear-gradient(180deg,#3c6d9c 0%,#2f5d88 50%,#1d3e5e 100%)" role="img" aria-label="Pelican resting by the water"></div>
  <div class="g" style="left:419px;top:4019px;width:239px;height:225px;background:linear-gradient(180deg,#eceef0 0%,#d6d9dd 55%,#b7b3ac 100%)" role="img" aria-label="Bright bedroom with ceiling fan"></div>
  <div class="g" style="left:667px;top:4019px;width:216px;height:225px;background:linear-gradient(90deg,#6a5a4c 0%,#d96a3a 40%,#3b8fc0 65%,#4a4038 100%)" role="img" aria-label="Colorful surfboard on the balcony"></div>
  <div class="g" style="left:892px;top:4019px;width:196px;height:225px;background:linear-gradient(180deg,#e6e7e8 0%,#c9c6c0 55%,#9d8f7d 100%)" role="img" aria-label="Living room with television and sofa"></div>
  <a class="read-more">READ MORE <svg width="18" height="18" viewBox="0 0 20 20"><circle cx="10" cy="10" r="8.5" stroke="#fff" stroke-width="1.5" fill="none"/><path d="M6 10h7M10 7l3 3-3 3" stroke="#fff" stroke-width="1.5" fill="none"/></svg></a>
</section>

<svg class="footer-shape" width="1200" height="650" viewBox="0 4300 1200 650">
  <path d="M0,4562 Q600,4318 1200,4562 L1200,4950 L0,4950 Z" fill="#000"/>
  <path d="M173,4500 Q606,4314 1040,4500 Q606,4350 173,4500 Z" fill="#1b6fb7"/>
</svg>

<footer>
  <h3 class="f-head" style="left:112px">Quick Links</h3>
  <ul class="f-list" style="left:114px">
    <li><svg width="12" height="10" viewBox="0 0 12 10"><path d="M0 5h9M6 1l4 4-4 4" stroke="#fff" stroke-width="2" fill="none"/></svg>Home</li>
    <li><svg width="12" height="10" viewBox="0 0 12 10"><path d="M0 5h9M6 1l4 4-4 4" stroke="#fff" stroke-width="2" fill="none"/></svg>About Us</li>
    <li><svg width="12" height="10" viewBox="0 0 12 10"><path d="M0 5h9M6 1l4 4-4 4" stroke="#fff" stroke-width="2" fill="none"/></svg>Menu</li>
    <li><svg width="12" height="10" viewBox="0 0 12 10"><path d="M0 5h9M6 1l4 4-4 4" stroke="#fff" stroke-width="2" fill="none"/></svg>Order Online</li>
    <li><svg width="12" height="10" viewBox="0 0 12 10"><path d="M0 5h9M6 1l4 4-4 4" stroke="#fff" stroke-width="2" fill="none"/></svg>What's New</li>
    <li><svg width="12" height="10" viewBox="0 0 12 10"><path d="M0 5h9M6 1l4 4-4 4" stroke="#fff" stroke-width="2" fill="none"/></svg>Contact Us</li>
  </ul>
  <h3 class="f-head" style="left:296px">Other Links</h3>
  <ul class="f-list" style="left:298px">
    <li><svg width="12" height="10" viewBox="0 0 12 10"><path d="M0 5h9M6 1l4 4-4 4" stroke="#fff" stroke-width="2" fill="none"/></svg>FAQ</li>
    <li><svg width="12" height="10" viewBox="0 0 12 10"><path d="M0 5h9M6 1l4 4-4 4" stroke="#fff" stroke-width="2" fill="none"/></svg>Terms of Use</li>
    <li><svg width="12" height="10" viewBox="0 0 12 10"><path d="M0 5h9M6 1l4 4-4 4" stroke="#fff" stroke-width="2" fill="none"/></svg>Privacy Policy</li>
    <li><svg width="12" height="10" viewBox="0 0 12 10"><path d="M0 5h9M6 1l4 4-4 4" stroke="#fff" stroke-width="2" fill="none"/></svg>Support Links</li>
    <li><svg width="12" height="10" viewBox="0 0 12 10"><path d="M0 5h9M6 1l4 4-4 4" stroke="#fff" stroke-width="2" fill="none"/></svg>Conditions</li>
  </ul>
  <h3 class="f-head" style="left:490px">Contact Us</h3>
  <div class="f-contact" style="top:4623px"><span class="dot"><svg width="14" height="18" viewBox="0 0 14 18"><path d="M7 1a6 6 0 0 1 6 6c0 4-6 10-6 10S1 11 1 7a6 6 0 0 1 6-6z" fill="#000"/><circle cx="7" cy="7" r="2" fill="#fff"/></svg></span>Company Name,United State.</div>
  <div class="f-contact" style="top:4684px"><span class="dot"><svg width="16" height="12" viewBox="0 0 16 12"><rect width="16" height="12" rx="1.5" fill="#000"/><path d="M1 1.5l7 5 7-5" stroke="#fff" stroke-width="1.4" fill="none"/></svg></span>info@companyname.in</div>
  <div class="f-contact" style="top:4744px"><span class="dot"><svg width="15" height="15" viewBox="0 0 24 24"><path fill="#000" d="M6.6 10.8a15 15 0 0 0 6.6 6.6l2.2-2.2a1 1 0 0 1 1-.25 11.4 11.4 0 0 0 3.6.57 1 1 0 0 1 1 1V20a1 1 0 0 1-1 1A17 17 0 0 1 3 4a1 1 0 0 1 1-1h3.5a1 1 0 0 1 1 1c0 1.25.2 2.45.57 3.57a1 1 0 0 1-.25 1z"/></svg></span>+1888 8888 8888</div>
  <h3 class="f-head" style="left:810px">Sign Up Our Newsletter</h3>
  <p class="news-copy">Lorem ipsum dolor sit amet,consectetur adipiscing elit,adipiscing elit.</p>
  <div class="news-label">Email</div>
  <div class="news-line"></div>
  <a class="subscribe">Subscribe</a>
  <div class="f-rule"></div>
  <p class="copyright">Copyrights@2025.Company Name.All Rights Reserved</p>
</footer>

</body>
</html>
```